Bramford Holloway Inc. needs an innovative idea for letterhead and visiting cards.

Bramford Holloway Inc. is a Canadian brand since 2007. It is a renown dealer of kids and office furniture locally. Moreover, exporting electric fixtures e.g. switches, LED's, down-lights etc. to Middle East and Africa. We have initiated a number of steps including re-branding, to boost our export in 2020. We have successfully designed our new logo a few months ago through 'Mockplanet' and now we are looking for an innovative idea for a letterhead.
Some key points:
• Red, black and white are the three colors used in all our packaging and furniture. (grey is optional)
• Shouldn’t be too wide.
• Use of watermark is preferable.
• You can visit our North American site at www.bramfordhollowayinc.com. Export website of the company will be launched soon. www.bramfordhollowayinc.ca
• Same letterhead will be used locally and internationally.
• Our new logo and sample packaging is attached.

```html
<!DOCTYPE html>
<html lang="en">
<head>
<meta charset="utf-8">
<title>Bramford Holloway Inc. Letterhead</title>
<link href="https://fonts.googleapis.com/css2?family=Open+Sans:wght@400;600;700&display=swap" rel="stylesheet">
<style>
  :root {
    --brand-red: #9e1b20;
    --ink: #2b2b2b;
    --ink-soft: #3c3c3c;
    --band-black: #231f20;
    --watermark: #e6e6e6;
    --backdrop: #d9d9d9;
    --paper: #ffffff;
    --rule: #cfcfcf;
  }
  * { margin: 0; padding: 0; box-sizing: border-box; }
  html, body { width: 1200px; height: 1113px; overflow: hidden; }
  body {
    background: var(--backdrop);
    font-family: "Open Sans", sans-serif;
    color: var(--ink);
    position: relative;
  }
  .letterhead {
    position: absolute;
    left: 285px; top: 126px;
    width: 605px; height: 849px;
    background: var(--paper);
    overflow: hidden;
  }
  .letterhead > * { position: absolute; }
  .band-top { left: 0; top: 0; }
  .band-bottom { right: 0; bottom: 0; }

  .brand { left: 78px; top: 62px; display: flex; align-items: center; gap: 8px; }
  .brand-mark { width: 30px; height: 30px; background: var(--brand-red); border-radius: 3px; }
  .brand-name { font-size: 15px; font-weight: 600; color: var(--ink-soft); letter-spacing: 0.3px; }

  .office-address {
    right: 212px; top: 70px;
    font-size: 7px; line-height: 12px; text-align: right; color: var(--ink);
  }
  .header-rule { left: 403px; top: 68px; width: 1px; height: 27px; background: var(--rule); }
  .office-contact { left: 414px; top: 67px; font-size: 7px; line-height: 13.5px; }
  .office-contact li { list-style: none; display: flex; align-items: center; gap: 6px; }
  .office-contact svg { width: 8px; height: 8px; fill: var(--brand-red); }

  .recipient { left: 78px; top: 192px; font-size: 9.5px; line-height: 15px; }
  .recipient-name { font-size: 10.5px; font-weight: 600; color: var(--brand-red); line-height: 14px; }
  .recipient-role { font-size: 7.5px; line-height: 13px; }
  .recipient-label { display: inline-block; width: 19px; font-weight: 700; color: var(--brand-red); }
  .recipient-label.is-dark { color: var(--ink); }
  .letter-date { right: 78px; top: 235px; font-size: 9.5px; }

  .letter-body { left: 78px; top: 281px; width: 460px; font-size: 9.5px; line-height: 19px; color: var(--ink-soft); }
  .letter-body p { margin-bottom: 19px; white-space: nowrap; }

  .signature-mark { left: 78px; top: 617px; width: 82px; height: 24px; background: linear-gradient(90deg, #e9e9e9, #f4f4f4); border-radius: 3px; }
  .signatory { left: 77px; top: 642px; font-size: 9.5px; line-height: 11px; }
  .signatory strong { display: block; font-weight: 700; }

  .watermark { left: 426px; top: 665px; width: 122px; height: 122px; border: 4px solid var(--watermark); border-radius: 12px; }

  .website { left: 402px; top: 810px; display: flex; align-items: center; gap: 7px; font-size: 9.5px; }
  .website svg { width: 12px; height: 12px; }
  .website strong { font-weight: 700; }
</style>
</head>
<body>
  <article class="letterhead">
    <svg class="band-top" width="240" height="12" viewBox="0 0 240 12"><polygon points="0,0 240,0 222,12 0,12" fill="var(--brand-red)"/></svg>

    <div class="brand">
      <span class="brand-mark"></span>
      <span class="brand-name">Bramford Holloway Inc.</span>
    </div>

    <address class="office-address" style="font-style:normal">240 Aldercrest Rd, Unit 18,<br>Maple Heights</address>
    <span class="header-rule"></span>
    <ul class="office-contact">
      <li><svg viewBox="0 0 24 24"><path d="M6.6 10.8a15 15 0 0 0 6.6 6.6l2.2-2.2a1 1 0 0 1 1-.25 11.4 11.4 0 0 0 3.6.57 1 1 0 0 1 1 1V20a1 1 0 0 1-1 1A17 17 0 0 1 3 4a1 1 0 0 1 1-1h3.5a1 1 0 0 1 1 1c0 1.25.2 2.45.57 3.57a1 1 0 0 1-.25 1z"/></svg>+1 (888) 555-0142</li>
      <li><svg viewBox="0 0 24 24"><path d="M2 5h20v14H2z M2 6l10 7 10-7" fill="var(--brand-red)" stroke="#fff" stroke-width="1.5"/></svg>sales@bramfordhollowayinc.com</li>
    </ul>

    <div class="recipient">
      <div class="recipient-name">Elsa Marrow</div>
      <div class="recipient-role">Manager</div>
      <div><span class="recipient-label">A :</span>27, Keller Street Australia - 4410</div>
      <div><span class="recipient-label is-dark">W :</span>enquiries@northpipe.net.au, northpipe.net.au</div>
      <div><span class="recipient-label">P :</span>0400 555 217</div>
    </div>
    <div class="letter-date">Date, 10 September, 2020</div>

    <div class="letter-body">
      <p>This is a sample letter that has been placed to demonstrate typing remat (Your Company). letterhead<br>design. When positioned properly, it will serve to work in harmony with all other elements letterhead.<br>This letterhead design is meant to project an image</p>
      <p>This letterhead design is meant project an image of professionalism reliability. By using simple aligen<br>we have created a very spacious feeling. The simplicity suggest&nbsp; rengththe spaciousnes contributes h<br>aesthetics the layout. These basic qualities along with te (Your Company)</p>
      <p>look and helps reinforce the (Your Company) brand. letterhead design is meant to project an image p<br>design. When positioned properly, it will serve to work in harmony all the other elements letterhead.<br>sionalism and reliability.</p>
      <p>This letterhead design is based on the (Form of your logo) form (Your Company) logo. Each stationery<br>we have created a very spacious feeling. The simplicity suggests strength the spaciousnes contribute<br>part of the (Form of your logo).</p>
    </div>

    <div class="signature-mark" role="img" aria-label="Handwritten signature of Elsa Marrow"></div>
    <div class="signatory"><strong>Elsa Marrow</strong>Manager</div>

    <div class="watermark" aria-hidden="true"></div>

    <div class="website">
      <svg viewBox="0 0 24 24"><circle cx="12" cy="12" r="10" fill="none" stroke="var(--brand-red)" stroke-width="2.2"/><path d="M2 12h20M12 2c3 3 3 17 0 20M12 2c-3 3-3 17 0 20" fill="none" stroke="var(--brand-red)" stroke-width="1.6"/></svg>
      <span>www.<strong>bramfordhollowayinc</strong>.com</span>
    </div>

    <svg class="band-bottom" width="240" height="13" viewBox="0 0 240 13"><polygon points="20,0 240,0 240,13 0,13" fill="var(--band-black)"/></svg>
  </article>
</body>
</html>
```